Rebuild

Hello,
I got a new logo, and a new business name. Now I need that new identity on a new web page.
Please take a look at my existing site. www.critterfixhub.com
and please build me a new website with my new logo and get it posted at my new domain www.tomvarlowcapture.com
Updates
Please include in the design the Radio marketing tagline "Tom Varlow, Raised and Ready for Wildlife Control".
I would like to add that it is usually understood that I will capture and remove problem causing animals. However, what I really need to emphasize is that I fortify homes and other structures to keep the animals out long term. Trapping is a temporary solution. Home fortification such as reinforcing vent screens, sealing holes, and constructing secure barriers is the Permanent solution. Kind of like a home security system for vertebrate pests. You don't really need an alarm system if you have the best locks and steel doors.
Obviously, my website is a multiple page website. Some designs will be good for the home page, and others for secondary pages.
Ultimately, I need a good home page that will attract clients, and then good backup pages to explain the different aspects of my work.
I imagine a home page. Sub pages would include Home Fortifications, Species detail pages, Company history, FAQs, Odd and unusual services, specialties, and where to go for the things I don't do. The text for these pages is something I can write myself. I'm a good writer. Just not a very good visual artist.
I have added the logo in .eps, and I have also added the mirror image logo in both eps and jpg. Let me know if other formats are needed.
I've posted a bunch of photos on my facebook for perusal
http://www.facebook.com/pages/Tom-Varlow-Wildlife-Control/902315748160334
Target Market(s)
Upper to middle income homeowners
Industry/Entity Type
Business
Look and feel
Each slider illustrates characteristics of the customer's brand and the style your logo design should communicate.

```html
<!DOCTYPE html>
<html lang="en">
<head>
<meta charset="utf-8">
<title>Tom Varlow Wildlife Control</title>
<link rel="stylesheet" href="https://fonts.googleapis.com/css2?family=Arimo:wght@400;700&family=Roboto+Condensed:wght@700&display=swap">
<style>
:root{
  --page:#f7f7f7;
  --ink:#4a4a4a;
  --body:#3a3a3a;
  --dark:#262626;
  --rule:#151515;
  --nav-rule:#0e0e0e;
  --accent:#f0c10c;
  --white:#ffffff;
  --muted:#bdbdbd;
  --soft:#8a8a8a;
  --more-dark:#6a6a6a;
  --frame:#9a9a9a;
}
*{box-sizing:border-box;margin:0;padding:0}
html,body{width:1095px;height:1200px;overflow:hidden;background:var(--page)}
body{font-family:"Arimo",Arial,sans-serif;color:var(--body);position:relative}
.site{position:absolute;left:43px;top:0;width:1010px;height:1200px}

.main-nav{position:absolute;top:5px;left:0;width:1010px;height:90px;background:var(--dark);display:flex;border-bottom:3px solid #ddd}
.main-nav a{display:flex;align-items:center;justify-content:center;color:var(--white);text-decoration:none;font-size:14px;text-transform:uppercase;border-right:2px solid var(--nav-rule)}
.main-nav a:last-child{border-right:none}
.main-nav a.is-current{color:var(--accent)}

.intro-card{position:absolute;top:106px;left:0;width:324px;height:365px;border:1px solid var(--frame);text-align:center}
.brand{position:absolute;top:118px;left:0;width:100%;display:flex;align-items:center;justify-content:center;gap:10px}
.brand-dot{width:22px;height:22px;border-radius:50%;background:var(--accent)}
.brand-name{font-family:"Arimo",Arial,sans-serif;font-weight:700;font-size:30px;color:var(--dark)}
.tagline{position:absolute;top:226px;left:0;width:100%}
.tagline-main{font-size:31px;color:var(--ink);line-height:1;letter-spacing:-.3px}
.tagline-sub{font-size:16px;font-style:italic;color:var(--soft);margin-top:2px}
.intro-card .more{position:absolute;top:300px;left:0;width:100%;justify-content:center}

.more{display:flex;align-items:baseline;gap:6px;font-family:"Roboto Condensed","Arial Narrow",sans-serif;font-weight:700;font-size:27px;letter-spacing:1px;color:var(--ink);text-decoration:none}
.more span{font-family:"Arimo",Arial,sans-serif;font-weight:400;font-size:15px}

.hero-photo{position:absolute;top:106px;left:335px;width:675px;height:365px;background:linear-gradient(180deg,#5c5a57 0%,#9b9894 35%,#8c8883 62%,#c9762a 82%,#e2c43a 100%)}

.features{position:absolute;top:503px;left:0;width:1010px}
.feature{position:absolute;top:0;width:305px}
.feature h2{font-size:24px;font-weight:700;color:var(--ink);line-height:1.2}
.feature .lead{font-size:15px;font-weight:700;color:var(--ink);line-height:25px;margin-top:12px}
.feature p{font-size:14px;line-height:22.5px;margin-top:11px;color:var(--body)}
.feature .more{margin-top:14px}

.band{position:absolute;top:824px;left:0;width:1010px;height:355px;background:var(--dark)}
.band-head{height:78px;border-bottom:2px solid var(--rule);position:relative}
.band-head h2{position:absolute;top:28px;font-size:33px;font-weight:400;color:var(--accent)}
.band-col{position:absolute;top:99px;width:270px}
.band-col .lead{font-size:15px;font-weight:700;color:var(--muted);line-height:25px}
.band-col p{font-size:14px;line-height:25px;color:var(--muted);margin-top:10px}
.band-col .more{color:var(--more-dark);margin-top:18px}
.band-foot{position:absolute;top:321px;left:0;width:100%;height:34px;border-top:2px solid var(--rule)}
.copyright{position:absolute;left:37px;top:8px;font-size:12px;color:var(--soft)}
</style>
</head>
<body>
<div class="site">
  <nav class="main-nav">
    <a class="is-current" style="width:119px">Home</a>
    <a style="width:147px">About Us</a>
    <a style="width:196px">Animal Control</a>
    <a style="width:207px">Wildlife Services</a>
    <a style="width:175px">Testimonials</a>
    <a style="width:166px">Contact Us</a>
  </nav>

  <section class="intro-card">
    <div class="brand"><span class="brand-dot"></span><span class="brand-name">Tom Varlow</span></div>
    <div class="tagline">
      <div class="tagline-main">RAISED AND READY</div>
      <div class="tagline-sub">FOR WILDLIFE CONTROL</div>
    </div>
    <a class="more">MORE <span>&gt;</span></a>
  </section>

  <div class="hero-photo" role="img" aria-label="Close-up photo of a raccoon's paw with long claws resting on grey fur"></div>

  <section class="features">
    <article class="feature" style="left:32px">
      <h2>Denique Pertinax Vix</h2>
      <div class="lead">Ea prompta conceptam maiestatis eum. Mei illud intellegam suscipiantur</div>
      <p>Cu nec velit postea tincidunt, ei sea electram dissentiet, vis at fugit putent tritani. Ius ea quod accusamus laboramus, sea id facilis probatus forensibus. Eos an quis graece salutatus, mea ex mutat libris quaeque. Platonem splendide definiebas nam in. Mea persius docendi et,</p>
      <a class="more">MORE <span>&gt;</span></a>
    </article>
    <article class="feature" style="left:366px">
      <h2>Denique Pertinax Vix</h2>
      <div class="lead">Ea prompta conceptam maiestatis eum. Mei illud intellegam suscipiantur</div>
      <p>Cu nec velit postea tincidunt, ei sea electram dissentiet, vis at fugit putent tritani. Ius ea quod accusamus laboramus, sea id facilis probatus forensibus. Eos an quis graece salutatus, mea ex mutat libris quaeque. Platonem splendide definiebas nam in. Mea persius docendi et,</p>
      <a class="more">MORE <span>&gt;</span></a>
    </article>
    <article class="feature" style="left:702px">
      <h2>Denique Pertinax Vix</h2>
      <div class="lead">Ea prompta conceptam maiestatis eum. Mei illud intellegam suscipiantur</div>
      <p>Cu nec velit postea tincidunt, ei sea electram dissentiet, vis at fugit putent tritani. Ius ea quod accusamus laboramus, sea id facilis probatus forensibus. Eos an quis graece salutatus, mea ex mutat libris quaeque. Platonem splendide definiebas nam in. Mea persius docendi et,</p>
      <a class="more">MORE <span>&gt;</span></a>
    </article>
  </section>

  <section class="band">
    <div class="band-head">
      <h2 style="left:34px">Aeterno</h2>
      <h2 style="left:365px">Nusquam</h2>
      <h2 style="left:700px">Concept</h2>
    </div>
    <div class="band-col" style="left:34px">
      <div class="lead">Ea prompta conceptam maiestatis eum. Mei illud intellegam</div>
      <p>Cu nec velit postea tincidunt, ei sea electram dissentiet, vis at fugit putent tritani. Ius ea quod accusamus laboramus, sea id facilis probatus forensibus. Eos an</p>
      <a class="more">MORE <span>&gt;</span></a>
    </div>
    <div class="band-col" style="left:368px">
      <div class="lead">Ea prompta conceptam maiestatis eum. Mei illud intellegam</div>
      <p>Cu nec velit postea tincidunt, ei sea electram dissentiet, vis at fugit putent tritani. Ius ea quod accusamus laboramus, sea id facilis probatus forensibus. Eos an</p>
      <a class="more">MORE <span>&gt;</span></a>
    </div>
    <div class="band-col" style="left:703px">
      <div class="lead">Ea prompta conceptam maiestatis eum. Mei illud intellegam</div>
      <p>Cu nec velit postea tincidunt, ei sea electram dissentiet, vis at fugit putent tritani. Ius ea quod accusamus laboramus, sea id facilis probatus forensibus. Eos an</p>
      <a class="more">MORE <span>&gt;</span></a>
    </div>
    <footer class="band-foot">
      <div class="copyright">Copyright © Tom Varlow Animal Control</div>
    </footer>
  </section>
</div>
</body>
</html>
```